Web Design For Staffing Company

We need a homepage web design for a technical staffing company.

Please see attached brief for project details.

please make the site modern with bold colors while matching the logo

Be sure to read the attached breif in full beforehand.

Target Market(s)

technical companies looking to hire talent

Industry/Entity Type

Staffing

Number of Pages Required

1 page

Font styles to use
Sans Serif

```html
<!DOCTYPE html>
<html lang="en">
<head>
<meta charset="utf-8">
<title>Veltrex Staffing — Technical Staffing</title>
<link href="https://fonts.googleapis.com/css2?family=Mulish:wght@400;600;700;800&display=swap" rel="stylesheet">
<style>
:root{
  --blue:#3d8fd8;
  --blue-title:#2f7dc6;
  --navy:#24537c;
  --band:#295e8b;
  --deep:#0f2f55;
  --ink:#222831;
  --text:#3b3f45;
  --muted:#6a6f76;
  --white:#ffffff;
}
*{margin:0;padding:0;box-sizing:border-box}
html,body{width:1200px;height:3974px;overflow:hidden;background:var(--white)}
body{font-family:"Mulish",Arial,sans-serif;color:var(--text)}
.canvas{position:relative;width:1200px;height:3974px;overflow:hidden;background:var(--white)}
.abs{position:absolute}
.btn{position:absolute;display:flex;align-items:center;justify-content:center;border-radius:22px;color:var(--white);font-weight:700;font-size:16px;gap:8px;white-space:nowrap}
.btn-light{background:var(--blue)}
.btn-dark{background:var(--navy)}

/* header */
.brand{position:absolute;left:142px;top:20px;display:flex;align-items:center;gap:10px;font-weight:800;font-size:34px;color:var(--navy);letter-spacing:-0.5px}
.brand-dot{width:16px;height:16px;border-radius:50%;background:var(--blue)}
.nav{position:absolute;top:34px;left:0;font-size:13px;color:var(--ink)}
.nav a{position:absolute;white-space:nowrap;color:var(--ink);text-decoration:none}
.nav a.active{color:var(--blue-title)}
.search{position:absolute;left:926px;top:25px;width:132px;height:34px;border:1px solid #cfd4da;font-size:12px;color:var(--muted);padding:9px 8px}
.search svg{position:absolute;right:8px;top:10px}

/* hero */
.hero-photo{position:absolute;left:0;top:83px;width:1200px;height:540px;background:linear-gradient(90deg,#ffffff 0%,#f1f2f4 30%,#c9ccd0 55%,#5f6670 75%,#8a8f96 100%)}
.hero-title{position:absolute;left:142px;top:172px;font-size:28px;line-height:40px;font-weight:800;color:var(--ink)}

/* intro */
.intro-shadow{position:absolute;left:205px;top:930px;width:790px;height:50px;background:#fff;box-shadow:0 4px 14px rgba(0,0,0,.12);border-radius:6px}
.intro{position:absolute;left:176px;top:711px;width:847px;height:250px;background:#fff;border-radius:6px;box-shadow:0 2px 14px rgba(0,0,0,.14);text-align:center;font-size:18px;line-height:33px;color:var(--ink);padding-top:46px;white-space:nowrap}

/* recruit */
.photo{position:absolute;border-radius:4px}
.h-blue{position:absolute;font-size:22px;font-weight:700;color:var(--blue-title)}
.para{position:absolute;font-size:15px;line-height:28px;color:var(--ink)}
.para b{color:var(--blue-title);font-weight:700}
.bullets{position:absolute;left:142px;top:1531px;width:520px;list-style:none;font-size:15px;line-height:28px;color:var(--ink)}
.bullets li{position:relative;padding-left:16px;margin-bottom:12px}
.bullets li::before{content:"";position:absolute;left:0;top:12px;width:6px;height:6px;border-radius:50%;background:var(--blue)}
.bullets b{color:var(--blue-title)}

/* testimonials */
.band{position:absolute;left:0;top:1918px;width:1200px;height:435px;background:var(--band)}
.band-title{position:absolute;left:142px;top:2048px;font-size:30px;line-height:28px;font-weight:700;color:#fff}
.band-copy{position:absolute;left:142px;top:2126px;width:370px;font-size:12px;line-height:19px;color:#e6eef6}
.band-link{position:absolute;left:142px;top:2218px;font-size:14px;font-weight:700;color:#fff;text-decoration:underline;display:flex;gap:8px;align-items:center}
.quote-card{position:absolute;left:555px;top:2024px;width:503px;height:217px;background:#fff;border-radius:6px;padding:28px 30px 0 54px;font-size:12px;line-height:25.5px;color:var(--ink)}
.quote-card .who{color:var(--blue-title);font-weight:700;font-size:15px}
.quote-card .who span{color:var(--ink);font-weight:400;font-size:11px}
.avatar{position:absolute;left:509px;top:1990px;width:79px;height:79px;background:#f0f2f5;border:3px solid #fff;box-shadow:0 2px 8px rgba(0,0,0,.25)}
.dot{position:absolute;top:2267px;width:14px;height:14px;border-radius:50%;background:#fff}
.dot.off{background:transparent;border:3px solid #fff}

/* blog */
.section-title{position:absolute;left:0;width:1200px;text-align:center;font-size:29px;font-weight:700;color:var(--ink)}
.post{position:absolute;top:2492px;width:294px;height:401px;background:#fff;box-shadow:0 2px 10px rgba(0,0,0,.13)}
.post-img{width:100%;height:188px}
.post-date{position:absolute;right:24px;top:22px;width:46px;height:56px;background:var(--blue);color:#fff;text-align:center;font-weight:800;font-size:18px;line-height:23px;padding-top:5px}
.post h3{margin:16px 18px 0;font-size:18px;line-height:24px;font-weight:600;color:var(--ink)}
.post p{margin:12px 18px 0;font-size:11.5px;line-height:20px;color:var(--text)}
.post .more{position:absolute;left:18px;bottom:37px;font-size:13px;font-weight:700;color:var(--blue-title);text-decoration:underline;display:flex;gap:6px;align-items:center}

/* cta */
.cta{position:absolute;top:3044px;height:324px;border-radius:6px;background:linear-gradient(135deg,#3a86cd,#2a6dae)}
.cta-frame{position:absolute;left:11px;top:11px;right:11px;bottom:11px;border:1.5px solid rgba(255,255,255,.55);border-radius:6px}
.cta h3{position:absolute;left:0;width:100%;top:180px;text-align:center;font-size:24px;line-height:32px;font-weight:700;color:#fff}
.cta .btn{top:252px;height:35px;font-size:15px}

/* footer */
.footer-top{position:absolute;left:0;top:3440px;width:1200px;height:16px;background:var(--deep)}
.footer-stripe{position:absolute;left:0;top:3456px;width:1200px;height:8px;background:#4a9be0}
.footer{position:absolute;left:0;top:3464px;width:1200px;height:510px;background:linear-gradient(100deg,#1d5187 0%,#2a69a8 60%,#3985cd 100%)}
.f-brand{position:absolute;left:142px;top:3568px;display:flex;align-items:center;gap:12px;font-size:50px;font-weight:800;color:#e9f1f9}
.f-head{position:absolute;top:3684px;font-size:17px;font-weight:700;color:#fff;white-space:nowrap}
.f-text{position:absolute;top:3722px;font-size:12px;line-height:23px;color:#dce8f4}
.f-btn{position:absolute;top:3820px;height:31px;border-radius:16px;background:#1d4d7e;color:#fff;font-size:12.5px;font-weight:700;display:flex;align-items:center;justify-content:center;gap:7px}
.social{position:absolute;left:944px;display:flex;align-items:center;gap:12px;font-size:12.5px;font-style:italic;color:#dce8f4}
.social i{width:28px;height:28px;border-radius:50%;border:1.5px solid #dce8f4}
.f-rule{position:absolute;left:142px;top:3915px;width:916px;height:1px;background:rgba(255,255,255,.3)}
.copy{position:absolute;left:0;top:3935px;width:1200px;text-align:center;font-size:12px;color:#dce8f4}
</style>
</head>
<body>
<div class="canvas">

  <!-- header -->
  <div class="brand"><span class="brand-dot"></span>Veltrex</div>
  <nav class="nav">
    <a class="active" style="left:511px">Home</a>
    <a style="left:580px">About</a>
    <a style="left:651px">Job Seekers</a>
    <a style="left:756px">Clients</a>
    <a style="left:830px">Contact Us</a>
  </nav>
  <div class="search">Search
    <svg width="12" height="12" viewBox="0 0 12 12"><circle cx="5" cy="5" r="3.8" fill="none" stroke="#333" stroke-width="1.5"/><path d="M8 8l3 3" stroke="#333" stroke-width="1.5"/></svg>
  </div>

  <!-- hero -->
  <div class="hero-photo" role="img" aria-label="Business team of three professionals reviewing tablets together"></div>
  <h1 class="hero-title">The Right People For The Right<br>Jobs! Bridging The Talent Gap<br>In Technical Staffing</h1>
  <div class="btn btn-light" style="left:142px;top:313px;width:133px;height:40px">Hire Talent</div>
  <div class="btn btn-dark" style="left:287px;top:313px;width:133px;height:40px">Get Hired</div>

  <!-- intro -->
  <div class="intro-shadow"></div>
  <div class="intro">
    Veltrex Staffing is a National Technical Staffing and Recruiting Solutions Provider founded<br>
    in 2013 focused on matching contract and full time Engineering and IT professionals<br>
    with new andexciting employment opportunities!
  </div>
  <div class="btn btn-dark" style="left:515px;top:872px;width:169px;height:37px">Contact Us Today</div>

  <!-- recruit -->
  <div class="photo" role="img" aria-label="Smiling colleagues in a meeting around a table" style="left:142px;top:1057px;width:367px;height:360px;background:linear-gradient(135deg,#b9c3cc,#7f8c97 60%,#5b6670)"></div>
  <h2 class="h-blue" style="left:560px;top:1082px">We Love To Recruit!</h2>
  <p class="para" style="left:560px;top:1120px;width:485px">It’s our passion and we take it very seriously! It is noteasy for <b>JOB SEEKERS</b> to put their job search efforts &amp; trust in the hands of someone else, especially when there are so many Staffing Firms to choose from. So how do you know you arechoosing the best Staffing Representation possible?</p>
  <p class="para" style="left:560px;top:1270px;width:485px">So how do you know you arechoosing the best Staffing Representation possible?</p>
  <div class="btn btn-light" style="left:560px;top:1347px;width:127px;height:39px">Learn More</div>
  <div class="btn btn-dark" style="left:697px;top:1347px;width:127px;height:39px">View Jobs</div>

  <!-- questions -->
  <ul class="bullets">
    <li>Are you responsible for Technical Staffing within your organization?</li>
    <li>Are you satisfied with yourcurrent Supplier(s)’ overall performance?</li>
    <li>Does it appear they identify potential Candidate(s)based purely on <b>“buzz-word”</b> searches?</li>
    <li>Is it evident they just do not grasp the scope andresponsibilities of your technical staffing need(s)?</li>
  </ul>
  <div class="btn btn-light" style="left:142px;top:1759px;width:125px;height:37px">Learn More</div>
  <div class="btn btn-dark" style="left:279px;top:1759px;width:125px;height:37px">Hire Talent</div>
  <div class="photo" role="img" aria-label="Smiling professional woman at a laptop with a colleague" style="left:693px;top:1487px;width:365px;height:360px;background:linear-gradient(135deg,#d6d9dc,#9aa3ab 55%,#5d6670)"></div>

  <!-- testimonials -->
  <div class="band"></div>
  <h2 class="band-title">What Employee<br>Say About</h2>
  <p class="band-copy">Lorem ipsum dolor sit amet, consectetuer adipiscing elit, sed diam nonummy nibh euismod tincidunt ut laoreet dolore mag na aliquam erat volutpat. Ut wisi enim ad minim veniam, quis nostrud exerci tation ullamcorper suscipit.</p>
  <div class="band-link">View All Testimonials
    <svg width="16" height="8" viewBox="0 0 16 8"><path d="M0 4h14M11 1l3 3-3 3" stroke="#fff" stroke-width="1.3" fill="none"/></svg>
  </div>
  <div class="quote-card">
    Marty Kellen is an excellent recruiter. He is articulate, honest, has a good nature and is aneffective information conduit between his clients and candidates. He gave me the feeling he is there for the big picture desiring to forge a future relationship that will be mutually beneficial to both of us.
    <div class="who">Sam R <span>- Electrical Test Engineer in the Automotive Sector</span></div>
    <svg class="abs" style="right:30px;bottom:20px" width="48" height="38" viewBox="0 0 48 38"><path d="M2 0h20v20L12 38H2l8-16H2z M26 0h20v20L36 38H26l8-16h-8z" fill="#2f7dc6"/></svg>
  </div>
  <div class="avatar" role="img" aria-label="Reviewer avatar placeholder"></div>
  <div class="dot" style="left:792px"></div>
  <div class="dot" style="left:814px"></div>
  <div class="dot off" style="left:835px"></div>

  <!-- blog -->
  <h2 class="section-title" style="top:2422px">Latest Blog Posts</h2>
  <article class="post" style="left:140px">
    <div class="post-img" role="img" aria-label="Woman working on a laptop" style="background:linear-gradient(135deg,#c8cbcf,#7b736c)"></div>
    <div class="post-date">17<br>JUN</div>
    <h3>Ways To Make The Most Of The Hot Job Market</h3>
    <p>This is the tightest labor market I can remember. Unemployment is at a 50-year low and wage growth is at 3.2%,” said...[+]</p>
    <div class="more">Read More <svg width="16" height="8" viewBox="0 0 16 8"><path d="M0 4h14M11 1l3 3-3 3" stroke="#2f7dc6" stroke-width="1.3" fill="none"/></svg></div>
  </article>
  <article class="post" style="left:452px">
    <div class="post-img" role="img" aria-label="Business handshake" style="background:linear-gradient(135deg,#dfe7ef,#6f93b5)"></div>
    <div class="post-date">06<br>JUN</div>
    <h3>Back To Basics: Meeting Employees’ Needs To Improve Organizational Performance</h3>
    <p>The benefits of employee satisfaction are well-established, so HR professionals...[+]</p>
    <div class="more">Read More <svg width="16" height="8" viewBox="0 0 16 8"><path d="M0 4h14M11 1l3 3-3 3" stroke="#2f7dc6" stroke-width="1.3" fill="none"/></svg></div>
  </article>
  <article class="post" style="left:765px">
    <div class="post-img" role="img" aria-label="Black and white portrait beside a quotation about technology" style="background:linear-gradient(135deg,#8a8a8a,#1e1e1e)"></div>
    <div class="post-date">20<br>JUN</div>
    <h3>5 Important Takeaways From Northwind’s Two-Year Study Of Remote Work</h3>
    <p>Recently, the folks at Northwind published their findings from a two-year study...[+]</p>
    <div class="more">Read More <svg width="16" height="8" viewBox="0 0 16 8"><path d="M0 4h14M11 1l3 3-3 3" stroke="#2f7dc6" stroke-width="1.3" fill="none"/></svg></div>
  </article>
  <div class="btn btn-dark" style="left:537px;top:2933px;width:126px;height:39px">View All</div>

  <!-- calls to action -->
  <div class="cta" style="left:142px;width:444px">
    <div class="cta-frame"></div>
    <svg class="abs" style="left:162px;top:44px" width="120" height="120" viewBox="0 0 120 120">
      <circle cx="60" cy="60" r="58" fill="none" stroke="#fff" stroke-width="2" stroke-dasharray="6 5"/>
      <circle cx="98" cy="16" r="4" fill="#fff"/><circle cx="22" cy="104" r="4" fill="#fff"/>
      <circle cx="60" cy="50" r="11" fill="none" stroke="#fff" stroke-width="2.5"/>
      <path d="M40 88c0-13 9-20 20-20s20 7 20 20" fill="none" stroke="#fff" stroke-width="2.5"/>
      <circle cx="35" cy="60" r="7" fill="none" stroke="#fff" stroke-width="2"/><circle cx="85" cy="60" r="7" fill="none" stroke="#fff" stroke-width="2"/>
    </svg>
    <h3>Looking For Career-Minded<br>Candidates?</h3>
    <div class="btn btn-dark" style="left:151px;width:142px">Request Talent</div>
  </div>
  <div class="cta" style="left:616px;width:442px">
    <div class="cta-frame"></div>
    <svg class="abs" style="left:161px;top:44px" width="120" height="120" viewBox="0 0 120 120">
      <circle cx="60" cy="60" r="58" fill="none" stroke="#fff" stroke-width="2" stroke-dasharray="6 5"/>
      <circle cx="98" cy="16" r="4" fill="#fff"/><circle cx="22" cy="104" r="4" fill="#fff"/>
      <circle cx="56" cy="46" r="12" fill="none" stroke="#fff" stroke-width="2.5"/>
      <path d="M34 86c0-14 10-22 22-22s22 8 22 22" fill="none" stroke="#fff" stroke-width="2.5"/>
      <rect x="66" y="74" width="20" height="14" fill="none" stroke="#fff" stroke-width="2"/>
    </svg>
    <h3>Looking For Career<br>Opportunities?</h3>
    <div class="btn btn-dark" style="left:152px;width:138px">Search Jobs</div>
  </div>

  <!-- footer -->
  <div class="footer-top"></div>
  <div class="footer-stripe"></div>
  <div class="footer"></div>
  <div class="f-brand"><span class="brand-dot" style="width:22px;height:22px;background:#e9f1f9"></span>Veltrex</div>

  <div class="f-head" style="left:142px">Find Jobs</div>
  <div class="f-text" style="left:142px">Search Our extensive<br>list of available jobs to find<br>your match.</div>
  <div class="f-btn" style="left:142px;width:121px">
    <svg width="12" height="12" viewBox="0 0 12 12"><circle cx="5" cy="5" r="3.8" fill="none" stroke="#fff" stroke-width="1.5"/><path d="M8 8l3 3" stroke="#fff" stroke-width="1.5"/></svg>Search Now</div>

  <div class="f-head" style="left:389px">Request An Employee</div>
  <div class="f-text" style="left:389px">We’re here to provide the people<br>you need to get work done.</div>
  <div class="f-btn" style="left:389px;width:121px">
    <svg width="12" height="12" viewBox="0 0 12 12"><circle cx="6" cy="3.5" r="2.8" fill="#fff"/><path d="M1 12c0-4 2.5-5.5 5-5.5s5 1.5 5 5.5z" fill="#fff"/></svg>Start Today</div>

  <div class="f-head" style="left:677px">Get In Touch</div>
  <div class="f-text" style="left:676px;line-height:18px">
    <svg width="10" height="13" viewBox="0 0 10 13" style="vertical-align:-2px"><path d="M5 0a5 5 0 0 1 5 5c0 4-5 8-5 8S0 9 0 5a5 5 0 0 1 5-5z" fill="#fff"/><circle cx="5" cy="5" r="1.8" fill="#2a69a8"/></svg>
    &nbsp;128 Harbor Lane, Suite 6,<br>&nbsp;&nbsp;&nbsp;&nbsp;&nbsp;3rd floor Millbrook,<br>&nbsp;&nbsp;&nbsp;&nbsp;&nbsp;MA 01999<br>
    <span style="display:inline-block;margin-top:8px"><svg width="12" height="12" viewBox="0 0 12 12" style="vertical-align:-2px"><path d="M2 0l2.5 3-1.3 1.6c.8 1.7 2.2 3 3.9 3.9L8.7 7.2 12 9.7 10.6 12C5 11.6.4 7 0 1.4z" fill="#fff"/></svg>&nbsp;555-014-2290</span>
  </div>
  <div class="f-btn" style="left:673px;width:120px">
    <svg width="12" height="9" viewBox="0 0 12 9"><rect width="12" height="9" fill="#fff"/><path d="M0 0l6 5 6-5" stroke="#1d4d7e" fill="none"/></svg>Contact Us</div>

  <div class="f-head" style="left:947px">Follow Us On</div>
  <div class="social" style="top:3720px"><i></i>Social Page</div>
  <div class="social" style="top:3762px"><i></i>Microposts</div>
  <div class="social" style="top:3805px"><i></i>Pro Network</div>

  <div class="f-rule"></div>
  <div class="copy">Copyright © 2020 Veltrex Staffing. All Rights Reserved.</div>
</div>
</body>
</html>
```